Tallowfen Associates Website

We need a website design for a UK based marketing and PR agency called "Tallowfen Associates". We are a small and vibrant team that looks after a mixture of clients from the luxury lifestyle and professional services sectors so the design needs to reflect this and convey: Professionalism, contemporary approach, creativity and the high end luxury and professional market we look after. Our services include marketing, PR, social media and copywriting and we look after both local and national clients. The design will need to incorporate the grey and orange brand colours (logo attached) but we are open to the use of more/different colours - with the possibility of a slight refresh on the current logo/branding. The main pages required include: Home, About Us, Services, Sectors, Case Studies and Blog.

ur existing website can be seen here - http://www.tallowfen.co.uk

The site will need to showcase our approach, services and expertise, existing/previous clients, and provide frequently updated content via news and blog to support our marketing campaigns.

The key objectives for the site are:
- To support current sales activity by giving potential clients somewhere to visit to find out who we are, what we can do, what we have done
- To generate incoming sales leads/enquiries from companies looking for marketing and PR services
- To showcase us as a high end a professional agency with some fantastic clients and a wealth of experience

Target Market(s)

Professional services e.g. accountants, data centres etc
Luxury lifestyle e.g. wedding venue, tailor, homeware etc.
British market - mainly South East/London
Small - Medium sized businesses

Industry/Entity Type

Marketing

Font styles to use
Other font styles liked:
• Din Regular and Bold is currently used

Colors
f78f20
aaaaaa

Requirements
Must have
• Must Have:
- The main menu items are likely to be:
- Services
- Sectors
- About us
- Case Studies
- Blog
- Contact us

Some of these items may have a sub-menu, e.g. About us is likely to have "Company", "Team", and "Careers" below it and "Services" will have "marketing", "PR", "Copywriting", "Social media". Sectors will have "Professional", "Luxury", "Lifestyle"

Key must-have elements of the homepage include:
- Social media icons (twitter, linkedin, facebook, google+)
- Contact details (i.e. phone number and email/link)
- "We have worked with..." - this is likely to be icons for logos of previous and current clients
- "Sign up to newsletter"
- "Latest news"

Footer navigation must allow for the usual suspects (sitemap, t's & c's, privacy policy, company registration details)

Some kind of call-to-action boxes/areas/links to provide us with ways to link out to any specific micro-sites or pages within the site (e.g. to highlight some of our specific case studies, services etc).

To confirm, we are looking for the following page types/templates:
1) Home page
2) Inside/content page (can be used for services, about us etc)
3) Article page (for blog/news articles etc)
4) Case studies (an image led pad to showcase campaigns we have worked on)
4) Contact page
Nice to have
• - If web fonts are needed for the design, then please note we have an existing web fonts account with typecrate.example and so can use any of the web fonts available there.
Should not have
• We do not want to use a one page-scroll down website

```html
<!DOCTYPE html>
<html lang="en">
<head>
<meta charset="utf-8">
<title>Tallowfen Associates – Marketing &amp; PR</title>
<link href="https://fonts.googleapis.com/css2?family=PT+Sans:wght@400;700&family=Roboto+Condensed:wght@400;500&display=swap" rel="stylesheet">
<style>
  :root {
    --orange: #f78f20;
    --orange-dark: #ec7a0c;
    --grey: #aaaaaa;
    --text: #4a4a4a;
    --text-soft: #8a8a8a;
    --line: #dcdcdc;
    --hero-bg: #f4f4f4;
    --footer-bg: #efefef;
    --white: #ffffff;
  }
  * { box-sizing: border-box; margin: 0; padding: 0; }
  html, body { width: 966px; height: 1200px; overflow: hidden; }
  body { background: var(--white); font-family: "PT Sans", Arial, sans-serif; color: var(--text); position: relative; }
  a { color: inherit; text-decoration: none; }

  .site-header { position: absolute; top: 0; left: 0; width: 966px; height: 97px; }
  .brand { position: absolute; left: 94px; top: 20px; color: var(--orange); font-size: 34px; line-height: 33px; }
  .brand span { display: block; font-size: 25px; line-height: 30px; }
  .contact-block { position: absolute; right: 89px; top: 40px; text-align: right; }
  .contact-phone { font-size: 22px; color: #555; display: flex; align-items: center; gap: 6px; justify-content: flex-end; }
  .contact-email { font-size: 13px; color: #666; display: flex; align-items: center; gap: 6px; justify-content: flex-end; margin-top: 2px; }

  .main-nav { position: absolute; left: 77px; top: 97px; width: 811px; height: 42px; background: linear-gradient(#fb9a35, var(--orange-dark)); display: flex; border-radius: 2px 2px 0 0; }
  .main-nav a { font-family: "Roboto Condensed", Arial, sans-serif; color: var(--white); font-size: 16px; letter-spacing: .5px; line-height: 42px; padding: 0 22px; border-right: 1px solid rgba(255,255,255,.35); }
  .main-nav a:last-child { border-right: 0; }
  .main-nav a:first-child { padding-left: 34px; padding-right: 23px; }

  .hero { position: absolute; top: 139px; left: 0; width: 966px; height: 307px; background: var(--hero-bg); border-top: 2px solid #eaeaea; border-bottom: 1px solid #e3e3e3; }
  .hero-kicker { position: absolute; left: 89px; top: 70px; color: var(--orange); font-size: 27px; }
  .hero-title { position: absolute; left: 88px; top: 100px; font-size: 39px; font-weight: 400; color: #444; }
  .hero-text { position: absolute; left: 92px; top: 150px; width: 345px; font-size: 12px; line-height: 19px; color: var(--text-soft); }
  .hero-dots { position: absolute; left: 93px; top: 199px; display: flex; gap: 4px; }
  .hero-dots i { width: 11px; height: 11px; border-radius: 50%; background: #d3d3d3; }
  .hero-dots i:first-child { background: var(--orange); }
  .hero-visual { position: absolute; left: 460px; top: 0; width: 430px; height: 305px; background: radial-gradient(ellipse at 55% 45%, #ffffff 0%, #ededed 75%, var(--hero-bg) 100%); }

  .welcome { position: absolute; top: 470px; left: 0; width: 966px; text-align: center; }
  .welcome h1 { font-size: 26px; font-weight: 400; color: #444; }
  .welcome p { width: 722px; margin: 6px auto 0; font-size: 11.6px; line-height: 19px; color: #5f5f5f; }

  .service-card { position: absolute; top: 592px; width: 264px; height: 197px; border: 1px solid var(--line); background: linear-gradient(#fff, #f6f6f6); }
  .service-card .photo { height: 130px; }
  .service-card h2 { font-size: 18px; font-weight: 400; color: #444; margin: 11px 0 0 17px; }
  .service-card p { font-size: 12.5px; color: var(--text-soft); margin: 2px 0 0 18px; }

  .news { position: absolute; left: 80px; top: 826px; width: 530px; }
  .news h2 { color: var(--orange); font-size: 23px; font-weight: 400; }
  .news-grid { display: grid; grid-template-columns: 269px 260px; row-gap: 16px; margin-top: 5px; }
  .news-item h3 { font-size: 13px; font-weight: 400; color: #444; margin-left: 3px; }
  .news-item p { font-size: 10.3px; line-height: 16px; color: var(--text-soft); margin: 3px 0 0 3px; width: 250px; }
  .news-item a { display: block; color: var(--orange); font-size: 11px; margin: 3px 0 0 3px; }

  .partners { position: absolute; left: 622px; top: 825px; width: 266px; height: 127px; border: 1px solid var(--line); }
  .partners h2 { font-size: 17px; font-weight: 400; color: #555; padding: 11px 0 0 20px; height: 40px; border-bottom: 1px solid var(--line); background: linear-gradient(#fff, #f5f5f5); }
  .partner-logos { display: flex; gap: 22px; padding: 22px 0 0 24px; }
  .partner-logos span { font-size: 16px; font-weight: 700; color: var(--orange); }
  .partners .arrows { position: absolute; right: 10px; bottom: 10px; }

  .newsletter { position: absolute; left: 622px; top: 961px; width: 266px; height: 93px; background: linear-gradient(#faa24a, var(--orange-dark)); border-radius: 2px; }
  .newsletter h2 { color: var(--white); font-size: 17px; font-weight: 400; margin: 14px 0 0 21px; }
  .newsletter .field { position: absolute; left: 21px; top: 41px; width: 219px; height: 25px; background: var(--white); border-radius: 2px; font-size: 10px; color: #888; line-height: 25px; padding-left: 10px; }
  .newsletter .field svg { position: absolute; right: 5px; top: 3px; }

  .site-footer { position: absolute; top: 1104px; left: 0; width: 966px; height: 96px; background: linear-gradient(#e9e9e9, #f7f7f7 30%); }
  .legal { position: absolute; left: 83px; top: 27px; font-size: 11px; color: #888; }
  .legal .sep { margin: 0 5px; }
  .copyright { position: absolute; left: 81px; top: 49px; font-size: 11px; color: #888; }
  .footer-nav { position: absolute; left: 395px; top: 26px; font-size: 12.2px; color: #444; }
  .footer-nav .sep { margin: 0 4px; }
  .social { position: absolute; left: 785px; top: 23px; display: flex; gap: 6px; }
  .social i { display: block; width: 20px; height: 20px; border-radius: 2px; }
</style>
</head>
<body>
  <header class="site-header">
    <a class="brand" href="#">Tallowfen<span>Associates</span></a>
    <div class="contact-block">
      <div class="contact-phone">
        <svg width="16" height="18" viewBox="0 0 16 18"><path d="M3 1 L6 1 L7 5 L5 7 Q7 11 10 13 L12 11 L15 12 L15 15 Q13 17 10 16 Q3 12 1 4 Q1 2 3 1Z" fill="#888"/></svg>
        01632 960 418
      </div>
      <div class="contact-email">
        <svg width="16" height="11" viewBox="0 0 16 11"><rect x="0.5" y="0.5" width="15" height="10" fill="#999"/><path d="M1 1 L8 6 L15 1" stroke="#fff" fill="none"/></svg>
        hello@tallowfen.co.uk
      </div>
    </div>
  </header>

  <nav class="main-nav">
    <a href="#">HOME</a><a href="#">ABOUT US</a><a href="#">SERVICES</a><a href="#">SECTORS</a><a href="#">CASE STUDIES</a><a href="#">BLOG</a><a href="#">CONTACT US</a>
  </nav>

  <section class="hero">
    <div class="hero-kicker">A Bright Approach to</div>
    <h1 class="hero-title">Your Marketing &amp; PR</h1>
    <p class="hero-text">Vivamus porttitor g purus nisi eleifend libero a tempus libero lectus feugiat felis Morbi diam mauris viverra in gravida</p>
    <div class="hero-dots"><i></i><i></i><i></i></div>
    <div class="hero-visual" role="img" aria-label="Illustration of a businessman drawing marketing sketches, charts and a city skyline on a white wall"></div>
  </section>

  <section class="welcome">
    <h1>Welcome to Tallowfen Associates</h1>
    <p>At Tallowfen Associates we have a strong background in providing marketing and PR services to clients across a broad range of sectors, both locally and international. Whatever you need; from on-going social media support, regular blogging and SEO copywriting to creative PR and marketing campaigns, we deliver a cost-effective and friendly service to boost your brand and business.</p>
  </section>

  <article class="service-card" style="left:79px">
    <div class="photo" role="img" aria-label="Photo of a business team presenting charts in a meeting" style="background:linear-gradient(135deg,#6f6f6f,#c8c8c8 55%,#8a8a8a)"></div>
    <h2>Marketing</h2><p>Phasellus felis dolor, scelerisque a tempus</p>
  </article>
  <article class="service-card" style="left:351px">
    <div class="photo" role="img" aria-label="Photo of a mentor with a headset helping a colleague at a computer" style="background:linear-gradient(135deg,#e8e4e0,#f4ede6 50%,#d9c7b4)"></div>
    <h2>PR Services</h2><p>Phasellus felis dolor, scelerisque a tempus</p>
  </article>
  <article class="service-card" style="left:622px">
    <div class="photo" role="img" aria-label="Photo of hands typing on a laptop on a wooden desk" style="background:linear-gradient(135deg,#b8713e,#d59966 50%,#a8612f)"></div>
    <h2>Copywriting</h2><p>Phasellus felis dolor, scelerisque a tempus</p>
  </article>

  <section class="news">
    <h2>Latest News</h2>
    <div class="news-grid">
      <div class="news-item"><h3>Mauris vel lacus vitae</h3><p>Vivamus porttitor, g, purus nisi eleifend libero, a tempus libero lectus feugiat felis. Morbi diam mauris, viverra in, gravida eu, mattis in, ante</p><a href="#">Learn More</a></div>
      <div class="news-item"><h3>Nullam enim leo</h3><p>Vivamus porttitor, g, purus nisi eleifend libero, a tempus libero lectus feugiat felis. Morbi diam mauris, viverra in, gravida eu, mattis in, ante</p><a href="#">Learn More</a></div>
      <div class="news-item"><h3>Consectetuer adipiscing</h3><p>Vivamus porttitor, g, purus nisi eleifend libero, a tempus libero lectus feugiat felis. Morbi diam mauris, viverra in, gravida eu, mattis in, ante</p><a href="#">Learn More</a></div>
      <div class="news-item"><h3>Phasellus felis dolor scelerisque</h3><p>Vivamus porttitor, g, purus nisi eleifend libero, a tempus libero lectus feugiat felis. Morbi diam mauris, viverra in, gravida eu, mattis in, ante</p><a href="#">Learn More</a></div>
    </div>
  </section>

  <aside class="partners">
    <h2>We have Worked with..</h2>
    <div class="partner-logos"><span>Brasswillow</span><span>Quillmarsh Books</span></div>
    <svg class="arrows" width="24" height="14" viewBox="0 0 24 14"><path d="M7 1 L1 7 L7 13 M17 1 L23 7 L17 13" stroke="#777" stroke-width="1.5" fill="none"/></svg>
  </aside>

  <aside class="newsletter">
    <h2>Newsletter Subscribe</h2>
    <div class="field">Email address
      <svg width="19" height="19" viewBox="0 0 19 19"><circle cx="9.5" cy="9.5" r="8" stroke="#f78f20" stroke-width="2" fill="none"/><path d="M5 9.5 H13 M10 6 L13.5 9.5 L10 13" stroke="#f78f20" stroke-width="2" fill="none"/></svg>
    </div>
  </aside>

  <footer class="site-footer">
    <div class="legal"><a href="#">Sitemap</a><span class="sep">|</span><a href="#">Privacy Policy</a><span class="sep">|</span><a href="#">Terms &amp; Conditions</a></div>
    <div class="copyright">Copyright © 2013 Tallowfen Ltd. All rights reserved</div>
    <nav class="footer-nav"><a href="#">Home</a><span class="sep">|</span><a href="#">About Us</a><span class="sep">|</span><a href="#">Services</a><span class="sep">|</span><a href="#">Sectors</a><span class="sep">|</span><a href="#">Case Studies</a><span class="sep">|</span><a href="#">Blog</a><span class="sep">|</span><a href="#">Contact us</a></nav>
    <div class="social">
      <i role="img" aria-label="Social network link" style="background:#3b5a9a"></i>
      <i role="img" aria-label="Social network link" style="background:#4fb3e6"></i>
      <i role="img" aria-label="Social network link" style="background:#2a7ab8"></i>
      <i role="img" aria-label="Social network link" style="background:#d9473a"></i>
    </div>
  </footer>
</body>
</html>
```